A4 Flyer

Brightwell Care Academy is starting a course in regional Victoria. We are currently advertising (See attached file A34984) in local papers but need to create a one page flyer to distribute to Aged Care facilities in the area. The A4 flyer will be inserted into a folder pack with more detailed information on Brightwell Care Academy. Important to use images and logoes attached

Target Market(s)

Flyer to be distributed to Aged Care facility staff and owners

Industry/Entity Type

Advertising

Font styles to use
Sans Serif

Colors
f37123
ec1f27

Requirements
Must have
• BCA Logo
Some image

```html
<!DOCTYPE html>
<html lang="en">
<head>
<meta charset="utf-8">
<title>Brightwell Care Academy – Fast Track Course Flyer</title>
<link rel="stylesheet" href="https://fonts.googleapis.com/css2?family=Arimo:ital,wght@0,400;0,700;1,400&family=Noto+Serif:wght@400;700&display=swap">
<style>
  :root {
    --orange: #f37123;
    --orange-deep: #e85a15;
    --red: #ec1f27;
    --yellow: #ffc914;
    --yellow-deep: #f5a800;
    --cream: #fdf5ec;
    --ink: #3d3d3d;
    --ink-soft: #555555;
    --grey-name: #6a6a6a;
    --stage: #e8e5e1;
    --white: #ffffff;
  }
  * { margin: 0; padding: 0; box-sizing: border-box; }
  html, body { width: 1200px; height: 1000px; overflow: hidden; }
  body {
    background: var(--stage);
    font-family: "Arimo", Arial, sans-serif;
    position: relative;
  }
  .flyer {
    position: absolute;
    left: 266px; top: 69px;
    width: 668px; height: 862px;
    background: var(--white);
    overflow: hidden;
    box-shadow: 0 6px 24px rgba(0,0,0,.25);
  }
  .content-bg {
    position: absolute; left: 0; top: 330px; width: 668px; height: 354px;
    background: linear-gradient(180deg, #fff8f0 0%, var(--cream) 60%, #fffaf5 100%);
  }
  .photo {
    position: absolute; top: 28px; height: 310px;
  }
  .photo--student-left {
    left: 0; width: 224px;
    background: linear-gradient(160deg, #eeeeee 0%, #d8d6d4 55%, #bdb6ae 100%);
    clip-path: polygon(0 0, 100% 0, 86% 100%, 0 100%);
  }
  .photo--trainer {
    left: 190px; width: 280px;
    background: linear-gradient(160deg, #f1eeea 0%, #e2c9bb 50%, #c98a6c 100%);
    clip-path: polygon(12% 0, 91% 0, 100% 100%, 0 100%);
  }
  .photo--student-right {
    left: 444px; width: 224px;
    background: linear-gradient(160deg, #f3f3f3 0%, #cfc8c4 55%, #4a3a3a 100%);
    clip-path: polygon(0 0, 100% 0, 100% 100%, 10% 100%);
  }
  .shapes { position: absolute; left: 0; top: 0; }
  .course-title {
    position: absolute; left: 36px; top: 399px;
    font-size: 20px; font-weight: 700; color: var(--orange);
  }
  .course-venue {
    position: absolute; left: 36px; top: 429px;
    font-size: 13.5px; font-style: italic; color: var(--ink-soft);
  }
  .divider {
    position: absolute; left: 35px; width: 598px;
    border-top: 2px dotted var(--orange);
  }
  .divider--top { top: 457px; }
  .divider--bottom { top: 634px; }
  .centered { position: absolute; left: 0; width: 668px; text-align: center; }
  .qual-label { top: 466px; font-size: 15px; color: var(--ink); }
  .qual-name { top: 485px; font-size: 16.5px; font-weight: 700; color: var(--ink); }
  .funding { top: 512px; font-size: 19px; font-weight: 700; color: var(--orange-deep); }
  .funding-note { top: 546px; left: -22px; font-size: 12px; color: var(--ink); }
  .topics { position: absolute; top: 567px; list-style: none; }
  .topics li {
    font-size: 13px; font-weight: 700; color: var(--ink);
    height: 21px; line-height: 21px; padding-left: 15px; position: relative;
  }
  .topics li::before {
    content: "✓"; position: absolute; left: 0; top: 0;
    color: var(--red); font-weight: 700;
  }
  .topics--a { left: 88px; }
  .topics--b { left: 273px; }
  .topics--c { left: 413px; }
  .mission {
    top: 644px; font-size: 11.5px; line-height: 16px; color: var(--ink);
  }
  .enrol {
    position: absolute; top: 684px; height: 35px; left: 0;
    display: flex; align-items: center; color: var(--white);
  }
  .enrol-label { position: absolute; left: 64px; font-size: 18px; letter-spacing: .3px; white-space: nowrap; }
  .enrol-label .arrow { font-size: 12px; vertical-align: 2px; }
  .enrol-url { position: absolute; left: 265px; font-size: 18.5px; font-weight: 700; white-space: nowrap; }
  .brand {
    position: absolute; left: 40px; top: 752px;
    display: flex; align-items: center; gap: 10px;
  }
  .brand-mark { width: 26px; height: 26px; border-radius: 50%; background: var(--orange); flex: none; }
  .brand-name {
    font-size: 20px; font-weight: 400; color: var(--grey-name); line-height: 24px; width: 170px;
  }
  .footer-rule {
    position: absolute; left: 289px; top: 738px; height: 72px;
    border-left: 1.5px solid var(--orange);
  }
  .call-label {
    position: absolute; left: 323px; top: 748px;
    font-family: "Noto Serif", Georgia, serif; font-size: 16px; font-weight: 700; color: var(--ink-soft);
  }
  .call-number {
    position: absolute; left: 322px; top: 768px;
    font-family: "Noto Serif", Georgia, serif; font-size: 27px; font-weight: 700; color: var(--ink);
  }
  .badge-text {
    position: absolute; text-align: center; line-height: 1.05;
  }
  .badge-text--unique {
    left: 425px; top: 307px; width: 120px;
    font-size: 18px; font-weight: 700; color: var(--orange-deep); transform: rotate(-6deg);
  }
  .badge-text--starts {
    left: 548px; top: 331px; width: 92px;
    font-size: 15px; color: var(--white); transform: rotate(-6deg);
  }
  .badge-text--enroll {
    left: 540px; top: 779px; width: 120px;
    font-size: 23px; font-weight: 700; color: var(--ink); transform: rotate(-6deg);
  }
</style>
</head>
<body>
<svg width="0" height="0" style="position:absolute" aria-hidden="true">
  <defs>
    <symbol id="burst" viewBox="-50 -50 100 100" preserveAspectRatio="none">
      <polygon points="50,0 41.5,11.1 43.3,25 30.4,30.4 25,43.3 11.1,41.5 0,50 -11.1,41.5 -25,43.3 -30.4,30.4 -43.3,25 -41.5,11.1 -50,0 -41.5,-11.1 -43.3,-25 -30.4,-30.4 -25,-43.3 -11.1,-41.5 0,-50 11.1,-41.5 25,-43.3 30.4,-30.4 43.3,-25 41.5,-11.1"/>
    </symbol>
    <linearGradient id="ribbon-fill" x1="0" y1="0" x2="0" y2="1">
      <stop offset="0" stop-color="#f7873a"/>
      <stop offset="1" stop-color="#e85a15"/>
    </linearGradient>
    <linearGradient id="yellow-fill" x1="0" y1="0" x2="0" y2="1">
      <stop offset="0" stop-color="#ffd836"/>
      <stop offset="1" stop-color="#f5a800"/>
    </linearGradient>
  </defs>
</svg>

<main class="flyer">
  <div class="content-bg"></div>

  <div class="photo photo--student-left" role="img" aria-label="Photo of a smiling mature male student in a white shirt holding papers in a classroom"></div>
  <div class="photo photo--trainer" role="img" aria-label="Photo of a female trainer pointing at an anatomical torso model"></div>
  <div class="photo photo--student-right" role="img" aria-label="Photo of a smiling young female student seated at a desk"></div>

  <svg class="shapes" width="668" height="862" viewBox="0 0 668 862" aria-hidden="true">
    <path d="M0,0 H668 V44 Q420,26 0,34 Z" fill="url(#ribbon-fill)"/>
    <path d="M0,34 Q420,26 668,44" fill="none" stroke="#fff" stroke-width="3"/>
    <line x1="224" y1="28" x2="192" y2="338" stroke="var(--orange)" stroke-width="2.5"/>
    <line x1="444" y1="28" x2="468" y2="338" stroke="var(--orange)" stroke-width="2.5"/>
    <path d="M0,310 Q334,322 668,370 L668,438 Q334,392 0,368 Z" fill="url(#ribbon-fill)"/>
    <path d="M0,316 Q334,328 668,376" fill="none" stroke="#fbb184" stroke-width="1.5"/>
    <text x="0" y="0" transform="translate(336,380) rotate(6.6)" text-anchor="middle"
          font-family="Arimo, Arial, sans-serif" font-weight="700" font-size="28" fill="#fff">Making You The Future Of Healthcare</text>
    <use href="#burst" x="425" y="288" width="125" height="85" fill="url(#yellow-fill)"/>
    <use href="#burst" x="543" y="318" width="100" height="72" fill="var(--orange)"/>
    <path d="M0,684 H618 L633,701.5 L618,719 H0 Z" fill="url(#ribbon-fill)"/>
    <path d="M0,830 Q320,846 668,810 V862 H0 Z" fill="url(#ribbon-fill)"/>
    <path d="M0,830 Q320,846 668,810" fill="none" stroke="#fbb184" stroke-width="2"/>
    <use href="#burst" x="525" y="742" width="158" height="118" fill="url(#yellow-fill)"/>
  </svg>

  <div class="badge-text badge-text--unique">Unique<br>Opportunity</div>
  <div class="badge-text badge-text--starts">Starts<br>July 2014</div>

  <h2 class="course-title">Fast Track Course</h2>
  <p class="course-venue">Rosehill Nursing Home – Stawell &nbsp;|&nbsp; 9:00am - 3:00pm</p>
  <div class="divider divider--top"></div>

  <p class="centered qual-label">Double Qualification</p>
  <h3 class="centered qual-name">CERT III IN AGED CARE WITH HOME AND COMMUNITY CARE</h3>
  <p class="centered funding">Government Funding for eligible students! Fees from $117</p>
  <p class="centered funding-note">This training is delivered with VIC and Comm Govt Funding to eligible students</p>

  <ul class="topics topics--a">
    <li>Pathology</li>
    <li>CPR</li>
    <li>Medications for PCA’s</li>
  </ul>
  <ul class="topics topics--b">
    <li>Aged Care</li>
    <li>Anaphylaxis</li>
    <li>Health Services</li>
  </ul>
  <ul class="topics topics--c">
    <li>First Aid</li>
    <li>Home &amp; Community Care</li>
  </ul>

  <div class="divider divider--bottom"></div>
  <p class="centered mission">Brightwell Care Academy aims to provide professional, accredited and accessible training<br>courses in order to increase your knowledge and strengthen your skills</p>

  <div class="enrol">
    <span class="enrol-label">TO ENROL VISIT <span class="arrow">▶</span></span>
    <span class="enrol-url">www.brightwellcare.com.au</span>
  </div>

  <div class="brand">
    <span class="brand-mark"></span>
    <span class="brand-name">Brightwell Care Academy</span>
  </div>
  <div class="footer-rule"></div>
  <p class="call-label">Call Us On</p>
  <p class="call-number">03 9555 0148</p>

  <div class="badge-text badge-text--enroll">Enroll<br>Now!!</div>
</main>
</body>
</html>
```